Aircraft maintenance buisness card

I am an aircraft mechanic looking for a personal buisness card . I would like my name and a title of Aircraft Maintenance Manager . I would like a suttle picture of an aircraft and helicopter .

elegant and professional wtih my contact .

My name should be on the car and Aircraft Maintenance Manager under with my contact infor below .

i have attached some pictures but i am open to other pics and ideas . I would like a airliner or private jet and a helicopter in the picture . The Images should be suttle and not the main idea . I also uploaded a picture of a jet engine which is cool . Be creative and i will work with you to finalize something .
Updates

Project Deadline Extended
Reason: Looking for more variations . Very good so far but looiking for a bit more styles and i uploaded my logo that i purchased . Please use my logo and be creative with it . I like some variations of black card with maybe some pictures that i uploaded but i am open to ideas . Be creative and i will work with you .

Project Deadline Extended
Reason: Looking for more designs and variations . Not yet satisfied with the designs i have gotten .

Industry/Entity Type

Aviation

Contact Information for Business Card

Aircraft Maintenance Manager

Font styles to use
Serif

Colors

Designer to choose colors to be used in the design.

Requirements
Must have
• An aviation related Logo if possible incorporated in the card possibly
• My name
• Tiberio Malvade Furtunato
• 482 Pellow St.
• Kearny , NJ
• 08519
• Email: Lwskyfixtech@mailvora.com
Nice to have
• Suttle Backround of a Private Jet or Airliner and a Helicopter .

```html
<!DOCTYPE html>
<html lang="en">
<head>
<meta charset="utf-8">
<title>Aircraft Maintenance Business Card</title>
<link href="https://fonts.googleapis.com/css2?family=Source+Serif+4:wght@300;400&display=swap" rel="stylesheet">
<style>
  :root {
    --backdrop: #1e1e1e;
    --card-black: #0c0c0c;
    --card-white: #ffffff;
    --accent-blue: #29abe2;
    --text-light: #f2f2f2;
    --text-grey: #3f3f3f;
    --photo-light: #7fa9c6;
    --photo-deep: #4a7592;
  }
  html, body {
    margin: 0;
    padding: 0;
    width: 1200px;
    height: 1000px;
    overflow: hidden;
    background: var(--backdrop);
    font-family: "Source Serif 4", Georgia, serif;
  }
  .stage {
    position: relative;
    width: 1200px;
    height: 1000px;
  }
  .card {
    position: absolute;
    top: 380px;
    width: 460px;
    height: 263px;
    box-shadow: 0 14px 30px rgba(0,0,0,0.55);
    overflow: hidden;
  }
  .card-back {
    left: 110px;
    background: var(--card-black);
  }
  .brand {
    position: absolute;
    left: 118px;
    top: 112px;
    display: flex;
    align-items: center;
    gap: 12px;
  }
  .brand-dot {
    width: 26px;
    height: 26px;
    border-radius: 50%;
    background: var(--accent-blue);
  }
  .brand-name {
    color: var(--text-light);
    font-size: 22px;
    font-weight: 400;
    white-space: nowrap;
  }
  .card-front {
    left: 630px;
    background: var(--card-white);
  }
  .cockpit-photo {
    position: absolute;
    left: 0;
    top: 0;
    width: 100%;
    height: 168px;
    background: linear-gradient(180deg, var(--photo-light) 0%, var(--photo-deep) 100%);
  }
  .details {
    position: absolute;
    left: 0;
    right: 0;
    bottom: 0;
    height: 95px;
    padding: 13px 18px 0 18px;
    box-sizing: border-box;
  }
  .person-name {
    margin: 0;
    color: var(--accent-blue);
    font-size: 19px;
    font-weight: 400;
    line-height: 1.15;
    white-space: nowrap;
  }
  .person-title {
    margin: 1px 0 0;
    color: var(--text-grey);
    font-size: 14px;
    font-weight: 300;
    line-height: 1.2;
    white-space: nowrap;
  }
  .contact {
    position: absolute;
    right: 18px;
    bottom: 12px;
    text-align: right;
    color: var(--text-grey);
    font-size: 13.5px;
    font-weight: 300;
    line-height: 1.35;
    white-space: nowrap;
  }
</style>
</head>
<body>
<main class="stage">
  <section class="card card-back">
    <div class="brand">
      <span class="brand-dot"></span>
      <span class="brand-name">Aircraft Maintenance</span>
    </div>
  </section>

  <section class="card card-front">
    <div class="cockpit-photo" role="img" aria-label="Photo: view from a helicopter cockpit over a city skyline"></div>
    <div class="details">
      <h1 class="person-name">Tiberio Malvade Furtunato</h1>
      <p class="person-title">Aircraft Maintenance Manager</p>
      <div class="contact">
        <div class="contact-email">Lwskyfixtech@mailvora.com</div>
        <div class="contact-address">482 Pellow St. Kearny, NJ 08519</div>
      </div>
    </div>
  </section>
</main>
</body>
</html>
```